Expensive Jewelery and Gold Website

I require a one page template design for my site PrimeMetalReplica.example. We sell replica gold bars. Not real ones, they are novelty gifts.

I have several images of the bars (attached)
I would like a stylish and professional template layout that will be used on my site.

Designed to appear to businesses and professionals and not the members of the public.

There is no idenity or artwork for the business so you may use whichever scheme you wish to. But must somehow stylish use the images or 2-3 of the images attached.

Target Market(s)

Business and marketing professional.

Industry/Entity Type

Business

Requirements
Must have
• Incorporate some or all of images
Nice to have
• Colour/styled images to match design and look in-keeping

```html
<!DOCTYPE html>
<html lang="en">
<head>
<meta charset="utf-8">
<title>PrimeMetalReplica.example</title>
<link rel="stylesheet" href="https://fonts.googleapis.com/css2?family=Almendra+SC&family=Arimo:wght@400;700&display=swap">
<style>
  :root {
    --page-red: #7e1409;
    --page-red-dark: #5e0d05;
    --column-cream: #f6e7bd;
    --column-light: #fbf3d9;
    --panel-tan: #e9d29b;
    --panel-edge: #d7b978;
    --frame-red: #9a1b0c;
    --title-red: #a3190c;
    --nav-red: #b5170a;
    --text-dark: #3a2a14;
    --rule: #9c1a0d;
    --divider: #d6b77a;
    --button-dark: #1b1208;
    --white: #ffffff;
  }
  * { box-sizing: border-box; margin: 0; padding: 0; }
  html, body { width: 796px; height: 1200px; overflow: hidden; }
  body {
    position: relative;
    font-family: "Arimo", Arial, sans-serif;
    color: var(--text-dark);
    background: radial-gradient(ellipse at center, var(--page-red) 0%, var(--page-red-dark) 100%);
  }
  .site {
    position: absolute; left: 40px; top: 0; width: 716px; height: 1168px;
    background: linear-gradient(180deg, var(--column-light) 0%, var(--column-cream) 22%, var(--column-cream) 100%);
  }
  .abs { position: absolute; }

  /* header */
  .brand-photo {
    left: 22px; top: 14px; width: 104px; height: 146px; border-radius: 6px;
    background: linear-gradient(160deg, #4a3a22 0%, #c99a3c 35%, #f1d68a 55%, #8a6020 80%, #3a2a14 100%);
    transform: rotate(-4deg);
    box-shadow: 0 4px 10px rgba(80,50,10,.35);
  }
  .brand-name {
    left: 146px; top: 52px; width: 236px; white-space: nowrap;
    font-family: "Almendra SC", Georgia, serif;
    font-size: 17px; line-height: 22px; color: var(--title-red);
  }
  .main-nav { right: 20px; top: 12px; display: flex; gap: 9px; font-size: 10px; font-weight: 700; }
  .main-nav a { color: #4a3515; text-decoration: none; }
  .main-nav a.current { color: var(--nav-red); }
  .main-nav span { color: #4a3515; }
  .search { left: 395px; top: 52px; display: flex; align-items: center; gap: 5px; }
  .search-field {
    width: 142px; height: 17px; border: 1px solid #d9b66a; background: #fbeec4;
    font-size: 9px; color: #b08a4a; text-align: center; line-height: 15px;
  }
  .search-go { width: 27px; height: 19px; background: var(--button-dark); color: var(--white); font-size: 10px; font-weight: 700; text-align: center; line-height: 19px; }

  /* main panel */
  .panel {
    left: 13px; top: 183px; width: 690px; height: 961px;
    background: var(--panel-tan); border: 2px solid var(--panel-edge); border-radius: 8px;
  }
  .slider { left: 26px; top: 196px; width: 667px; height: 269px; background: var(--frame-red); padding: 7px; }
  .slide-photo {
    width: 100%; height: 100%;
    background: linear-gradient(100deg, #b7b0a6 0%, #e9e6e0 25%, #c8c2b8 45%, #5a564f 62%, #2a2724 75%, #b08032 85%, #3a2f22 100%);
  }
  .slide-dots { left: 37px; top: 442px; display: flex; gap: 2px; }
  .slide-dots span { width: 11px; height: 11px; background: #efe6d2; color: #333; font-size: 8px; line-height: 11px; text-align: center; }
  .slide-dots span.on { background: var(--frame-red); color: var(--white); }

  /* categories */
  .categories { left: 33px; top: 476px; width: 115px; }
  .categories h2 { font-size: 19px; color: var(--title-red); margin: 0 0 6px 7px; }
  .categories li {
    list-style: none; height: 22px; line-height: 22px; font-size: 10px; font-weight: 700;
    border-bottom: 1px dashed var(--rule); padding-left: 10px; position: relative;
  }
  .categories li::before { content: ""; position: absolute; left: 0; top: 8px; width: 6px; height: 4px; background: #b48a4a; transform: skewX(-30deg); }

  /* articles */
  .card { width: 145px; }
  .card-photo { height: 86px; margin: 0 4px; border: 2px solid var(--white); box-shadow: 0 1px 3px rgba(0,0,0,.25); }
  .card h3 { font-size: 9px; color: var(--title-red); text-align: center; margin: 8px 0 4px; line-height: 11px; height: 22px; }
  .card p { font-size: 8.5px; line-height: 11px; text-align: justify; height: 170px; overflow: hidden; }
  .row2 h3 { height: 33px; }
  .row2 p { height: 154px; }
  .read-more {
    display: block; width: 56px; height: 16px; margin: 6px 0 0 auto; background: var(--button-dark);
    color: var(--white); font-size: 9px; font-weight: 700; text-align: center; line-height: 16px;
    border: 1px solid #6a5a3a;
  }
  .divider { width: 1px; background: var(--divider); }

  .footer { left: 0; top: 1176px; width: 796px; text-align: center; font-size: 9px; font-weight: 700; color: var(--white); }
</style>
</head>
<body>
  <div class="site">
    <div class="abs brand-photo" role="img" aria-label="Photo of a gold replica bar"></div>
    <div class="abs brand-name">PrimeMetalReplica.example</div>
    <nav class="abs main-nav">
      <a class="current" href="#">HOME</a><span>||</span>
      <a href="#">REGISTER</a><span>||</span>
      <a href="#">LOGIN</a><span>||</span>
      <a href="#">MEDIA</a><span>||</span>
      <a href="#">JOBS</a><span>||</span>
      <a href="#">CONTACT</a><span>||</span>
      <a href="#">ABOUT US</a><span>||</span>
      <a href="#">SITEMAP</a>
    </nav>
    <div class="abs search">
      <svg width="22" height="22" viewBox="0 0 22 22" aria-hidden="true">
        <circle cx="9" cy="9" r="6" fill="#cfe4f2" stroke="#6a7f90" stroke-width="2"/>
        <line x1="13.5" y1="13.5" x2="20" y2="20" stroke="#5a4a30" stroke-width="3" stroke-linecap="round"/>
      </svg>
      <div class="search-field">- Enter Your Search Words -</div>
      <div class="search-go">Go</div>
    </div>

    <div class="abs panel"></div>
    <div class="abs slider"><div class="slide-photo" role="img" aria-label="Photo of a wrapped gift box beside a gold replica bar on dark velvet"></div></div>
    <div class="abs slide-dots"><span class="on">1</span><span>2</span><span>3</span><span>4</span><span>5</span></div>

    <aside class="abs categories">
      <h2>Categories</h2>
      <ul>
        <li>British Gold</li><li>Bullion Coins</li><li>Bullion Vault</li><li>Fake</li>
        <li>FAQ</li><li>Fort Knox</li><li>Fraud</li><li>Gold</li><li>Gold Bars</li>
        <li>Gold Bullion</li><li>Gold Bullion Trading</li><li>Gold Guide</li>
      </ul>
    </aside>

    <div class="abs divider" style="left:177px;top:480px;height:300px"></div>
    <div class="abs divider" style="left:346px;top:480px;height:300px"></div>
    <div class="abs divider" style="left:524px;top:480px;height:300px"></div>
    <div class="abs divider" style="left:177px;top:808px;height:312px"></div>
    <div class="abs divider" style="left:346px;top:808px;height:312px"></div>
    <div class="abs divider" style="left:524px;top:808px;height:312px"></div>

    <article class="abs card" style="left:188px;top:475px">
      <div class="card-photo" role="img" aria-label="Photo of a steel safe with its door open" style="background:linear-gradient(135deg,#e8e8e8,#9a9ea2 60%,#5e6266);border-color:transparent;box-shadow:none"></div>
      <h3>Keeping Your Gold Bullion Safe</h3>
      <p>A popular way to hold value in a rapidly changing world is to keep gold close at hand. Many people think of the bar shape when they hear the word bullion, yet it also comes as coins and rounds. Storing it well matters, because a bar kept in a drawer is easy to lose and hard to insure. A proper safe, a bank box or a vault service each give peace of mind.</p>
      <span class="read-more">Read More</span>
    </article>
    <article class="abs card" style="left:356px;top:475px">
      <div class="card-photo" role="img" aria-label="Line chart of the gold price rising over time" style="background:linear-gradient(180deg,#ffffff,#f3f3f3)"></div>
      <h3>Some abcs on Gold Bullion Trading</h3>
      <p>If you have thought about trading in gold bullion but were not sure where to begin, here is some basic guidance. Gold can be bought or sold much like any other product that trades on an open market. Some dealers work only in bars while others prefer coins. Most buyers purchase at wholesale prices and later sell when prices rise.</p>
      <span class="read-more">Read More</span>
    </article>
    <article class="abs card" style="left:534px;top:475px">
      <div class="card-photo" role="img" aria-label="Photo of a stone depository building under a pale sky" style="background:linear-gradient(180deg,#e6ecf0 0%,#d8dde0 45%,#9a8a72 70%,#6e6a52 100%)"></div>
      <h3>Fort knox the us Gold Bullion Depository</h3>
      <p>Most people have heard of Fort Knox and associate it with gold bars. The depository is a secure site where the nation keeps a large share of its gold reserves along with other valued records. An interesting fact is that it was built in the thirties and has rarely opened its doors to visitors since that time.</p>
      <span class="read-more">Read More</span>
    </article>

    <article class="abs card row2" style="left:188px;top:808px">
      <div class="card-photo" role="img" aria-label="Photo of a person holding a stacked gold bar" style="background:linear-gradient(120deg,#3a2414,#b8863a 45%,#e8c56a 60%,#7a4a22)"></div>
      <h3>gold bullion vault and storage the real largest gold bullion vault in the world</h3>
      <p>When you mention gold bullion most people think of Fort Knox. While a great deal of gold is stored there, it is not the largest depository in the world. Deep beneath the streets of New York sits a vault that holds bars from many nations, cut into solid bedrock far below the subway system. Its walls are thick steel.</p>
      <span class="read-more">Read More</span>
    </article>
    <article class="abs card row2" style="left:356px;top:808px">
      <div class="card-photo" role="img" aria-label="Photo of a gold bar in an open wooden presentation case" style="background:linear-gradient(160deg,#d8d2c8,#8a4a26 45%,#5a2a14 75%,#c8a060)"></div>
      <h3>gold bullion history lesson gold bullion through the ages</h3>
      <p>Gold has been one of the most precious metals in the world since mankind first looked for things to use for trade. Ancient cultures made tablets and statues of gold, and many believed it was a gift from the gods. For this reason it was highly valued and often used to adorn temples, crowns and the finest jewellery of each age.</p>
      <span class="read-more">Read More</span>
    </article>
    <article class="abs card row2" style="left:534px;top:808px">
      <div class="card-photo" role="img" aria-label="Photo of gold coins spread in a pile" style="background:linear-gradient(140deg,#6a4a14,#d6ae4a 40%,#f0d68a 55%,#9a7424)"></div>
      <h3>Gold Bullion Investments using Gold Bullion Coins as part of your Portfolio</h3>
      <p>When you decide to invest your money to increase the value of your portfolio, you have many choices. Stocks, bonds, precious metals and other options are all open to you. One such option is gold bullion coins, which have kept their value over long periods when the economy has fluctuated. Gold bullion coins are coins minted for investors.</p>
      <span class="read-more">Read More</span>
    </article>
  </div>

  <footer class="abs footer">© Copyright 2010-2011 PrimeMetalReplica.example . All Right Reserved</footer>
</body>
</html>
```